Cd Cover design for Chicago based record label.

Cd Cover design for a new single! Song is dedicated to exotic dancers. We do not want our artist pictures on this one. So please use your imagination. Song Title: "Velvet Hours". Thanks? Artist: Ray Castellan feat. Lil Trevane.

```html
<!DOCTYPE html>
<html lang="en">
<head>
<meta charset="utf-8">
<title>Velvet Hours – Single Cover</title>
<link rel="stylesheet" href="https://fonts.googleapis.com/css2?family=Orbitron:wght@500&display=swap">
<style>
  :root {
    --night-navy: #1a1f3d;
    --deep-plum: #3a2140;
    --ember-red: #b8332c;
    --amber-glow: #f08a3c;
    --neon-red: #ff1a0a;
    --neon-halo: rgba(255, 20, 0, 0.75);
    --neon-band: rgba(220, 20, 10, 0.55);
    --spotlight: #f8f1f1;
    --dancer-hot: #ff4a4a;
    --dancer-warm: #f4805c;
    --pole-red: #ff3c42;
  }
  html, body {
    margin: 0;
    padding: 0;
    width: 1200px;
    height: 1200px;
    overflow: hidden;
    background: var(--night-navy);
  }
  .cover {
    position: relative;
    width: 1200px;
    height: 1200px;
    overflow: hidden;
    background:
      radial-gradient(circle at 100% 24%, var(--amber-glow) 0%, rgba(240,138,60,0.6) 16%, rgba(184,51,44,0.55) 36%, rgba(58,33,64,0) 62%),
      radial-gradient(ellipse at 52% 28%, rgba(184,51,44,0.5) 0%, rgba(184,51,44,0) 48%),
      linear-gradient(135deg, var(--deep-plum) 0%, var(--night-navy) 55%, #131833 100%);
  }
  .title-glow {
    position: absolute;
    left: 130px;
    top: 212px;
    width: 740px;
    height: 100px;
    background: var(--neon-band);
    filter: blur(22px);
    border-radius: 20px;
  }
  .song-title {
    position: absolute;
    left: 154px;
    top: 212px;
    margin: 0;
    font-family: "Orbitron", sans-serif;
    font-weight: 500;
    font-size: 66px;
    line-height: 1;
    letter-spacing: 5px;
    white-space: nowrap;
    text-transform: uppercase;
    color: var(--neon-red);
    transform: scaleY(1.5);
    transform-origin: left top;
    text-shadow:
      0 0 4px var(--neon-halo),
      0 0 14px var(--neon-halo),
      0 0 30px rgba(255, 20, 0, 0.5);
  }
  .stage {
    position: absolute;
    inset: 0;
  }
</style>
</head>
<body>
  <main class="cover">
    <div class="title-glow"></div>
    <h1 class="song-title">Velvet Hours</h1>
    <svg class="stage" width="1200" height="1200" viewBox="0 0 1200 1200">
      <defs>
        <clipPath id="spotClip">
          <circle cx="840" cy="816" r="360"/>
        </clipPath>
        <radialGradient id="dancerFill" cx="0.5" cy="0.45" r="0.5">
          <stop offset="0" stop-color="var(--dancer-hot)" stop-opacity="0.95"/>
          <stop offset="0.6" stop-color="var(--dancer-warm)" stop-opacity="0.7"/>
          <stop offset="1" stop-color="var(--dancer-warm)" stop-opacity="0"/>
        </radialGradient>
      </defs>
      <circle class="spotlight" cx="840" cy="816" r="360" fill="var(--spotlight)"/>
      <g clip-path="url(#spotClip)">
        <ellipse class="dancer-figure" role="img" aria-label="Silhouette of a pole dancer arching backwards with long hair, holding the pole"
                 cx="955" cy="860" rx="210" ry="330" fill="url(#dancerFill)"/>
      </g>
      <rect class="dance-pole" x="996" y="0" width="11" height="1200" fill="var(--pole-red)"/>
    </svg>
  </main>
</body>
</html>
```